I have just launched a labour hire company and lookingfor a fresh vibrant website design

I need a landing page, a description of our services and capability, as well as an enquiries link, and register candidates link. My company is called Kestrel9 recruitment and we supply labourers, excavator operators, and machine operators to the Civil and railway industries. I would like to stick to our logo theme and colours of Bright green, although I want a brighter green please than what I have. I have attached Images I like as well plaese. I do need a much bigger website eventually.

```html
<!DOCTYPE html>
<html lang="en">
<head>
<meta charset="utf-8">
<title>Kestrel9 Recruitment – NSW Civil &amp; Rail Labour Specialists</title>
<link href="https://fonts.googleapis.com/css2?family=Poppins:wght@400;500;600;700&display=swap" rel="stylesheet">
<style>
:root{
  --green:#0b5e17;
  --green-bright:#12a51f;
  --green-text:#0e6a1a;
  --ink:#222;
  --muted:#4a4a4a;
  --grey-panel:#efeded;
  --field:#e9e9e9;
  --white:#fff;
  --dark:#1c1b18;
}
*{box-sizing:border-box;margin:0;padding:0}
html,body{width:1200px;height:4598px;overflow:hidden}
body{position:relative;font-family:"Poppins",sans-serif;color:var(--ink);background:var(--white)}
.abs{position:absolute}

/* header */
.site-header{left:0;top:0;width:1200px;height:110px}
.brand{left:50px;top:34px;display:flex;align-items:center;gap:10px;font-weight:600;font-size:20px;color:var(--green)}
.brand-mark{width:16px;height:16px;background:var(--green-bright)}
.main-nav{right:78px;top:34px;display:flex;align-items:center;gap:17px;font-size:14.5px;color:var(--green-text);font-weight:500}
.nav-cta{border:2px solid var(--green-text);padding:4px 8px;border-radius:2px}

/* hero */
.hero{left:0;top:110px;width:1200px;height:535px;background:linear-gradient(180deg,#7a5a1e 0%,#6b4c17 45%,#3b2a10 75%,#1b140a 100%)}
.hero-title{left:0;width:1200px;top:60px;text-align:center;color:var(--white);font-weight:700;font-size:40px;line-height:56px}
.hero-sub{left:150px;width:900px;top:186px;text-align:center;color:var(--white);font-weight:600;font-size:25px;line-height:38px}
.btn{display:flex;align-items:center;justify-content:center;font-size:19px;font-weight:500}
.btn-light{left:367px;top:312px;width:214px;height:56px;background:var(--white);color:#222}
.btn-ghost{left:615px;top:312px;width:215px;height:56px;border:2px solid var(--white);color:var(--white)}

/* about */
.section-title{font-size:31px;font-weight:600;color:var(--green-text);text-align:center}
.section-title::after{content:"";display:block;height:4px;background:var(--green-text);margin:6px auto 0}
.about-title{left:116px;top:712px;text-align:left}
.about-title::after{width:136px;margin-left:0}
.about-text{left:117px;top:808px;width:520px;font-size:17.5px;line-height:28.3px;color:var(--muted)}
.about-photo{left:790px;top:645px;width:410px;height:582px;background:linear-gradient(160deg,#8a8f9c,#5b6170 60%,#6b6a60)}
.about-circle{left:662px;top:760px;width:352px;height:352px;border-radius:50%;border:7px solid var(--white);background:radial-gradient(circle at 40% 45%,#dfe3e8,#e2762b 45%,#8f8a78 80%)}

/* services */
.services-title{left:0;width:1200px;top:1297px}
.services-title::after{width:132px}
.services-intro{left:230px;width:740px;top:1366px;text-align:center;font-size:20px;line-height:28.5px;color:var(--muted)}
.tile{position:absolute;width:369px}
.tile-green{background:var(--green);color:var(--white);padding:0 37px}
.tile-photo{}
.tile h3{font-size:25px;font-weight:600;margin-bottom:12px}
.tile p{font-size:19.5px;line-height:28.5px}
.tile svg{display:block;margin-bottom:14px}

/* why */
.why-title{left:0;width:1200px;top:2255px}
.why-title::after{width:176px}
.why-lead{left:160px;width:390px;top:2350px;text-align:center;font-size:25px;font-weight:600;line-height:33px;color:var(--green-text)}
.why-circle{left:262px;top:2447px;width:222px;height:222px;border-radius:50%;background:radial-gradient(circle at 50% 70%,#a8532b,#c98b4d 45%,#9fb2bf 80%)}
.why-text{left:128px;width:490px;top:2698px;text-align:center;font-size:20.5px;line-height:31px;color:var(--muted)}
.why-panel{left:693px;top:2378px;width:477px;height:507px;background:var(--grey-panel)}
.checklist{list-style:none;left:750px;top:2477px;font-size:21px;color:#222}
.checklist li{display:flex;align-items:center;gap:17px;height:68.4px}

/* contact */
.contact{left:84px;top:2933px;width:1033px;height:645px;background:linear-gradient(180deg,#5a4a2a 0%,#4a3d24 40%,#262219 70%,var(--dark) 100%)}
.contact-title{left:84px;width:440px;top:3040px;text-align:center;font-size:40px;font-weight:600;color:var(--white)}
.contact-text{left:130px;width:365px;top:3127px;text-align:center;font-size:20.5px;line-height:31px;color:var(--white)}
.socials{left:206px;top:3392px;display:flex;gap:26px}
.socials span{width:36px;height:36px;border-radius:50%;display:block}
.enquiry{left:568px;top:2997px;width:474px;height:485px;background:var(--green);border-radius:30px}
.enquiry h2{position:absolute;left:0;width:100%;top:30px;text-align:center;color:var(--white);font-size:25px;font-weight:500}
.field{position:absolute;left:59px;width:357px;height:52px;background:var(--field);border-radius:8px;font-size:14.5px;color:#333;padding:0 17px;display:flex;align-items:center;font-weight:500}
.field-msg{height:108px;align-items:flex-start;padding-top:18px}
.enquiry-btn{position:absolute;left:59px;top:393px;width:141px;height:42px;background:#111;color:var(--white);border-radius:5px;font-size:14.5px;display:flex;align-items:center;justify-content:center;font-weight:500}

/* testimonials */
.testi-title{left:0;width:1200px;top:3615px}
.testi-title::after{width:112px}
.testi-photo{width:172px;height:172px;border-radius:50%}
.testi-name{font-size:26px;color:var(--green-text);font-weight:500}
.testi-role{font-size:17px;color:#222;font-weight:500}
.testi-quote{width:580px;font-size:14.5px;line-height:24px;color:var(--muted)}

/* footer */
.site-footer{left:0;top:4215px;width:1200px;height:383px;background:var(--green)}
.footer-brand{left:103px;top:96px;width:284px;height:140px;background:var(--white);display:flex;align-items:center;justify-content:center;gap:10px;font-size:20px;font-weight:600;color:var(--green)}
.footer-col{top:78px;color:var(--white);font-size:18px}
.footer-col h4{font-weight:500;font-size:18px;margin-bottom:25px}
.footer-col li{list-style:none;display:flex;align-items:center;gap:8px;height:34px}
.footer-col li::before{content:"";width:11px;height:11px;border:2.5px solid var(--white);border-radius:50%;background:radial-gradient(circle,var(--white) 35%,transparent 40%)}
.footer-rule{left:0;top:300px;width:1200px;height:1px;background:rgba(255,255,255,.35)}
.copyright{left:0;width:1200px;top:320px;text-align:center;color:var(--white);font-size:18px}
</style>
</head>
<body>

<header class="site-header abs">
  <div class="brand abs"><span class="brand-mark"></span>Kestrel9 Recruitment</div>
  <nav class="main-nav abs">
    <span>Home</span><span>About us</span><span>Services</span><span>Enquiries</span><span>Contact</span>
    <span class="nav-cta">Register Candidate</span>
  </nav>
</header>

<section class="hero abs" role="img" aria-label="Excavator silhouette against a golden sunset over a civil worksite">
  <h1 class="hero-title abs">NSW CIVIL &amp; RAIL LABOUR SPECIALISTS<br>LABOUR SPECIALISTS</h1>
  <p class="hero-sub abs">Kestrel9 Recruitment is a NSW labour hire agency specialising in the civil sector. With a strong track record of providing skilled</p>
  <span class="btn btn-light abs">Read More</span>
  <span class="btn btn-ghost abs">Services</span>
</section>

<section class="about">
  <h2 class="section-title about-title abs">About us</h2>
  <p class="about-text abs">Lorem ipsum dolor sit amet, consectetur adipiscing elit, sed do eiusmod tempor incididunt ut labore et dolore magna aliqua. Quis ipsum suspendisse ultrices gravida. Risus commodo viverra maecenas accumsan lacus vel facilisis. Lorem ipsum dolor sit amet, consectetur adipiscing elit, sed do eiusmod tempor incididunt ut labore et dolore magna aliqua. Quis ipsum suspendisse ultrices gravida. Risus commodo viverra maecenas accumsan lacus vel facilisis. amet, consectetur adipiscing elit, sed do eiusmod tempor incididunt ut labore et dolore magna aliqua. Quis ipsum suspendisse ultrices gravida. Risus commodo viverra maecenas accumsan lacus vel facilisis.</p>
  <div class="about-photo abs" role="img" aria-label="Building sketch and safety helmets on a construction plan"></div>
  <div class="about-circle abs" role="img" aria-label="Safety helmets, house model and tape measure on blueprints"></div>
</section>

<section class="services">
  <h2 class="section-title services-title abs">Services</h2>
  <p class="services-intro abs">Lorem ipsum dolor sit amet, consectetur adipiscing elit, sed do eiusmod tempor incididunt ut labore et dolore magna aliqua. Quis ipsum suspendisse ultrices gravida. Risus commodo viverra maecenas</p>

  <div class="tile tile-photo" style="left:50px;top:1500px;height:370px;background:linear-gradient(135deg,#6d6a66,#9a958e 50%,#5c5853)" role="img" aria-label="Railway tracks on gravel ballast"></div>
  <div class="tile tile-green" style="left:419px;top:1500px;height:304px;padding-top:28px">
    <svg width="70" height="76" viewBox="0 0 70 76" aria-hidden="true"><g fill="none" stroke="#fff" stroke-width="4"><rect x="24" y="6" width="40" height="66"/><rect x="6" y="28" width="18" height="44"/></g><g fill="#fff"><rect x="33" y="16" width="8" height="8"/><rect x="47" y="16" width="8" height="8"/><rect x="33" y="32" width="8" height="8"/><rect x="47" y="32" width="8" height="8"/><rect x="33" y="48" width="8" height="8"/><rect x="47" y="48" width="8" height="8"/><rect x="11" y="38" width="8" height="8"/><rect x="11" y="54" width="8" height="8"/></g></svg>
    <h3>Roads</h3>
    <p>Lorem ipsum dolor sit amet, consectetur adipiscing elit, sed do eiusmod tempor</p>
  </div>
  <div class="tile tile-photo" style="left:787px;top:1500px;height:370px;background:linear-gradient(160deg,#c9a55a,#a37a3f 50%,#5a4630)" role="img" aria-label="Dump truck and excavator inside a tunnel construction site"></div>

  <div class="tile tile-green" style="left:50px;top:1870px;height:318px;padding-top:38px">
    <svg width="66" height="76" viewBox="0 0 66 76" aria-hidden="true"><g fill="none" stroke="#fff" stroke-width="3.5"><path d="M20 18a13 13 0 0 1 26 0z"/><path d="M16 18h34"/><circle cx="33" cy="28" r="8"/><path d="M12 58l6-18h30l6 18z"/><rect x="6" y="58" width="54" height="12"/><path d="M24 46l18 10M42 46l-18 10"/></g></svg>
    <h3>Railways</h3>
    <p>Lorem ipsum dolor sit amet, consectetur adipiscing elit, sed do eiusmod tempor</p>
  </div>
  <div class="tile tile-photo" style="left:419px;top:1804px;height:384px;background:linear-gradient(180deg,#b9c9d6 0%,#cfd8de 45%,#d9582a 60%,#9c9a92 85%)" role="img" aria-label="Two orange excavators on a road site"></div>
  <div class="tile tile-green" style="left:787px;top:1870px;height:318px;padding-top:38px">
    <svg width="80" height="66" viewBox="0 0 80 66" aria-hidden="true"><g fill="none" stroke="#fff" stroke-width="3.5"><ellipse cx="36" cy="20" rx="16" ry="12"/><path d="M20 20v8h32v-8"/><path d="M8 32h52l6 10H8z"/><circle cx="22" cy="52" r="7"/><circle cx="54" cy="52" r="7"/><path d="M60 28h10v14"/><path d="M8 32v22"/></g></svg>
    <h3>Tunnels</h3>
    <p>Lorem ipsum dolor sit amet, consectetur adipiscing elit, sed do eiusmod tempor</p>
  </div>
</section>

<section class="why">
  <h2 class="section-title why-title abs">why choose us</h2>
  <p class="why-lead abs">Our company has many years of experience!</p>
  <div class="why-circle abs" role="img" aria-label="Excavator loading a truck with red soil"></div>
  <p class="why-text abs">As a result of our philosophy to be the most forward thinking home cleaning company and our focus on understanding customer needs, we have and will continue to expand across the UK with franchises .</p>
  <div class="why-panel abs"></div>
  <ul class="checklist abs">
    <li><svg width="34" height="34" viewBox="0 0 34 34" aria-hidden="true"><rect x="2" y="2" width="30" height="30" rx="3" fill="none" stroke="#0e6a1a" stroke-width="3.5"/><path d="M9 17l6 6 11-12" fill="none" stroke="#0e6a1a" stroke-width="3.5"/></svg>Industry Experience</li>
    <li><svg width="34" height="34" viewBox="0 0 34 34" aria-hidden="true"><rect x="2" y="2" width="30" height="30" rx="3" fill="none" stroke="#0e6a1a" stroke-width="3.5"/><path d="M9 17l6 6 11-12" fill="none" stroke="#0e6a1a" stroke-width="3.5"/></svg>Skill Assessment</li>
    <li><svg width="34" height="34" viewBox="0 0 34 34" aria-hidden="true"><rect x="2" y="2" width="30" height="30" rx="3" fill="none" stroke="#0e6a1a" stroke-width="3.5"/><path d="M9 17l6 6 11-12" fill="none" stroke="#0e6a1a" stroke-width="3.5"/></svg>Reference Checking</li>
    <li><svg width="34" height="34" viewBox="0 0 34 34" aria-hidden="true"><rect x="2" y="2" width="30" height="30" rx="3" fill="none" stroke="#0e6a1a" stroke-width="3.5"/><path d="M9 17l6 6 11-12" fill="none" stroke="#0e6a1a" stroke-width="3.5"/></svg>ICompliance Verification</li>
    <li><svg width="34" height="34" viewBox="0 0 34 34" aria-hidden="true"><rect x="2" y="2" width="30" height="30" rx="3" fill="none" stroke="#0e6a1a" stroke-width="3.5"/><path d="M9 17l6 6 11-12" fill="none" stroke="#0e6a1a" stroke-width="3.5"/></svg>Rigorous Selection Process</li>
  </ul>
</section>

<section class="contact-block">
  <div class="contact abs" role="img" aria-label="Silhouetted workers and machinery on a dusky construction site"></div>
  <h2 class="contact-title abs">Get In Touch</h2>
  <p class="contact-text abs">As a result of our philosophy to be the most forward thinking home cleaning company and our focus on understanding customer needs, we have and will continue to expand across the UK with franchises .</p>
  <div class="socials abs" aria-label="Social links">
    <span style="background:#1d9bf0"></span><span style="background:#c2318d"></span><span style="background:#3a5aa8"></span>
  </div>
  <form class="enquiry abs">
    <h2>Enquires</h2>
    <div class="field" style="top:88px">Enter Your Name</div>
    <div class="field" style="top:173px">Enter your valid Email</div>
    <div class="field field-msg" style="top:259px">Message</div>
    <span class="enquiry-btn">Enquire Now</span>
  </form>
</section>

<section class="testimonials">
  <h2 class="section-title testi-title abs">Testimonials</h2>

  <div class="testi-photo abs" style="left:186px;top:3722px;background:linear-gradient(160deg,#e9ecef,#b9c2cc 55%,#2a4d8c)" role="img" aria-label="Portrait of contractor in a blue suit"></div>
  <div class="testi-name abs" style="left:372px;top:3726px">Marcus Delaney</div>
  <div class="testi-role abs" style="left:372px;top:3759px">Contractor</div>
  <p class="testi-quote abs" style="left:372px;top:3800px">Lorem ipsum dolor sit amet, consectetur adipiscing elit, sed do eiusmod tempor incididunt ut labore et dolore magna aliqua. Quis &nbsp;maecenas accumsan lacus vel facilisis.</p>

  <div class="testi-photo abs" style="left:186px;top:3954px;background:linear-gradient(160deg,#8a2a25,#b3493d 50%,#d9c2ad)" role="img" aria-label="Portrait of architect on the phone"></div>
  <div class="testi-name abs" style="left:368px;top:3958px">Tomas Renner</div>
  <div class="testi-role abs" style="left:370px;top:3991px">Architecture</div>
  <p class="testi-quote abs" style="left:372px;top:4032px">Lorem ipsum dolor sit amet, consectetur adipiscing elit, sed do eiusmod tempor incididunt ut labore et dolore magna aliqua. Quis &nbsp;maecenas accumsan lacus vel facilisis.</p>
</section>

<footer class="site-footer abs">
  <div class="footer-brand abs"><span class="brand-mark"></span>Kestrel9 Recruitment</div>
  <div class="footer-col abs" style="left:487px">
    <h4>Quick Links</h4>
    <ul><li>Home</li><li>About us</li><li>services</li><li>enquiries</li></ul>
  </div>
  <div class="footer-col abs" style="left:680px">
    <h4>Services</h4>
    <ul><li>Terms</li><li>Privacy Policy</li><li>Useful Terms</li></ul>
  </div>
  <div class="footer-col abs" style="left:890px">
    <h4>Follow us</h4>
    <ul><li>Social Feed</li><li>Photo Wall</li><li>Microblog</li></ul>
  </div>
  <div class="footer-rule abs"></div>
  <p class="copyright abs">All &nbsp;Rights &nbsp;reserved . Copyrights @ 2023</p>
</footer>

</body>
</html>
```